BrivoLane Ute.

I want the full logo on one side. And the other side the card if right Ralf the logo the left half orange like the car in the logo color with Danielle R Morrow
Founder and CEO
Email symbol then dmorrow@brivolaneute.com
Www symbol. Then Brivolaneute.com
Phone symbol then 413-926-BRIV
The very bottom would like Brivo Lane Ute is a division of Harmond Vistas. LLC

```html
<!DOCTYPE html>
<html lang="en">
<head>
<meta charset="utf-8">
<title>Brivo Lane Ute – Business Card</title>
<link href="https://fonts.googleapis.com/css2?family=Montserrat:wght@700&family=Overpass:wght@400;600&display=swap" rel="stylesheet">
<style>
  :root {
    --orange: #e68c1f;
    --orange-dark: #b06e1e;
    --orange-light: #eaa24c;
    --brown: #3d2a0e;
    --ink: #111111;
    --white: #ffffff;
  }
  * { margin: 0; padding: 0; box-sizing: border-box; }
  html, body { width: 1200px; height: 1200px; overflow: hidden; }
  body {
    background: radial-gradient(circle at 50% 50%, #3a3a3c 0%, #1a1a1a 45%, #000 85%);
    font-family: "Overpass", sans-serif;
  }
  .stage { width: 1500px; height: 1500px; position: relative; transform: scale(0.8); transform-origin: 0 0; }
  .card { position: absolute; left: 370px; width: 760px; height: 465px; background: var(--white); overflow: hidden; }
  .card-front { top: 173px; }
  .card-back { top: 886px; }

  .front-panel { position: absolute; left: 0; top: 0; width: 317px; height: 100%; background: var(--orange); }
  .name-band { position: absolute; left: 0; top: 67px; width: 384px; height: 79px; background: var(--brown); }
  .name-fold { position: absolute; left: 317px; top: 146px; width: 67px; height: 27px; }
  .name { position: absolute; right: 92px; top: 10px; font-family: "Montserrat", sans-serif; font-weight: 700; font-size: 24px; color: var(--white); white-space: nowrap; }
  .title { position: absolute; right: 92px; top: 47px; font-family: "Overpass", sans-serif; font-weight: 600; font-size: 17px; color: var(--white); white-space: nowrap; }

  .contact { position: absolute; right: 444px; font-size: 18px; color: var(--ink); white-space: nowrap; line-height: 1; }
  .contact-email { top: 241px; right: 484px; }
  .contact-web { top: 300px; right: 481px; }
  .contact-phone { top: 357px; right: 479px; }
  .icon { position: absolute; left: 302px; width: 28px; height: 28px; }
  .icon-email { top: 238px; }
  .icon-web { top: 295px; }
  .icon-phone { top: 352px; }

  .side-strip { position: absolute; right: 0; top: 0; width: 33px; height: 100%; background: var(--brown); }
  .pill { position: absolute; left: 0; width: 33px; border-radius: 16px; }
  .pill-outer { top: 37px; height: 390px; background: var(--orange-dark); }
  .pill-mid { top: 87px; height: 290px; background: var(--orange); }
  .pill-inner { top: 140px; height: 184px; background: var(--orange-light); }

  .logo-front { position: absolute; left: 380px; top: 150px; width: 280px; text-align: center; }
  .brand-art { display: block; margin: 0 auto 10px; }
  .brand-name { font-family: "Overpass", sans-serif; font-weight: 600; color: var(--ink); white-space: nowrap; }
  .logo-front .brand-name { font-size: 32px; }
  .division { position: absolute; left: 380px; top: 396px; width: 280px; text-align: center; font-size: 17px; line-height: 22px; color: var(--ink); }

  .border-band { position: absolute; left: 38px; width: 684px; height: 12px; background: var(--orange); border-radius: 6px; }
  .border-top { top: 22px; }
  .border-bottom { top: 440px; }
  .logo-back { position: absolute; left: 0; top: 110px; width: 100%; text-align: center; }
  .logo-back .brand-name { font-size: 48px; }
</style>
</head>
<body>
<main class="stage">
  <section class="card card-front">
    <div class="front-panel"></div>
    <div class="name-band">
      <p class="name">Danielle R Morrow</p>
      <p class="title">Founder &amp; CEO</p>
    </div>
    <svg class="name-fold" viewBox="0 0 67 27"><polygon points="0,0 67,0 0,27" fill="#b06e1e"/></svg>

    <p class="contact contact-email">dmorrow@brivolaneute.com</p>
    <svg class="icon icon-email" viewBox="0 0 28 28"><circle cx="14" cy="14" r="14" fill="#fff"/><rect x="7" y="9" width="14" height="10" fill="none" stroke="#e68c1f" stroke-width="1.6"/><polyline points="7,9 14,15 21,9" fill="none" stroke="#e68c1f" stroke-width="1.6"/></svg>

    <p class="contact contact-web">Brivolaneute.com</p>
    <svg class="icon icon-web" viewBox="0 0 28 28"><circle cx="14" cy="14" r="14" fill="#fff"/><g fill="none" stroke="#e68c1f" stroke-width="1.4"><circle cx="14" cy="14" r="8"/><ellipse cx="14" cy="14" rx="3.5" ry="8"/><line x1="6" y1="14" x2="22" y2="14"/><line x1="7.5" y1="10" x2="20.5" y2="10"/><line x1="7.5" y1="18" x2="20.5" y2="18"/></g></svg>

    <p class="contact contact-phone">413-926-BRIV</p>
    <svg class="icon icon-phone" viewBox="0 0 28 28"><circle cx="14" cy="14" r="14" fill="#fff"/><path d="M9 7.5 L12 7.5 L13 11 L11.2 12.3 C12 14.5 13.5 16 15.7 16.8 L17 15 L20.5 16 L20.5 19 C20.5 20 19.5 20.5 18.5 20.5 C12.5 20 8 15.5 7.5 9.5 C7.5 8.5 8 7.5 9 7.5 Z" fill="#e68c1f"/><path d="M16 8 A5 5 0 0 1 20 12" fill="none" stroke="#e68c1f" stroke-width="1.3"/></svg>

    <div class="logo-front">
      <svg class="brand-art" width="200" height="90" viewBox="0 0 200 90" role="img" aria-label="Illustration area: station wagon with surfboard and bottles beside a fence">
        <defs><linearGradient id="artFront" x1="0" y1="0" x2="0" y2="1"><stop offset="0" stop-color="#f6d9b0"/><stop offset="1" stop-color="#e68c1f"/></linearGradient></defs>
        <rect width="200" height="90" rx="6" fill="url(#artFront)"/>
      </svg>
      <p class="brand-name">Brivo Lane Ute</p>
    </div>
    <p class="division">Brivo Lane Ute is a division<br>of Harmond Vistas. LLC</p>

    <div class="side-strip">
      <div class="pill pill-outer"></div>
      <div class="pill pill-mid"></div>
      <div class="pill pill-inner"></div>
    </div>
  </section>

  <section class="card card-back">
    <div class="border-band border-top" role="img" aria-label="Ornamental orange flourish border"></div>
    <div class="logo-back">
      <svg class="brand-art" width="290" height="130" viewBox="0 0 290 130" role="img" aria-label="Illustration area: station wagon with surfboard and bottles beside a fence">
        <defs><linearGradient id="artBack" x1="0" y1="0" x2="0" y2="1"><stop offset="0" stop-color="#f6d9b0"/><stop offset="1" stop-color="#e68c1f"/></linearGradient></defs>
        <rect width="290" height="130" rx="8" fill="url(#artBack)"/>
      </svg>
      <p class="brand-name">Brivo Lane Ute</p>
    </div>
    <div class="border-band border-bottom" role="img" aria-label="Ornamental orange flourish border"></div>
  </section>
</main>
</body>
</html>
```